Trade Show Booth Sign Design for Retracting Banner

I need a trade show booth sign designed. It will be for a retractable banner that is double sided with 34 by 81 inch.

I want to incorporate my logo (see attached, have it in other file formats as well) and graphics from my website (https://www.dolbrookteachingadvisory.com/) with parts or all of the following text.

· Educational Content Creation
o Supplemental Textbook Content Development
o E-learning Content Development
· Curriculum Development
o KVTR/Bright Ladder
o Three Dimensional Learning
· Assessment
o Formative Assessments
o Elementary School, Middle School, High School, College, and Business
· Professional Development
o Training
o Facilitation

Target Market(s)

Education

Industry/Entity Type

Education

Font styles to use
Sans Serif

Colors

Designer to choose colors to be used in the design.

Requirements
Must have
• Eye catching and easy to read design
Nice to have
• Would like to see incorporation of my logo and some of the elements of my website images
Should not have
• N/A

```html
<!DOCTYPE html>
<html lang="en">
<head>
<meta charset="UTF-8">
<title>Dolbrook Teaching Advisory – Retractable Banner</title>
<link href="https://fonts.googleapis.com/css2?family=Questrial&display=swap" rel="stylesheet">
<style>
  :root {
    --stage: #d9d9d9;
    --banner: #ffffff;
    --brand-blue: #1677ee;
    --brand-navy: #0d2470;
    --chart-light: #eef2f8;
    --chart-dark: #13306f;
    --chalkboard: #3b3b3b;
    --chalkboard-dark: #2c2c2c;
    --photo-warm: #e6d3c4;
    --photo-cool: #9fb6cc;
  }
  * { margin: 0; padding: 0; box-sizing: border-box; }
  html, body {
    width: 1200px;
    height: 1200px;
    overflow: hidden;
    background: var(--stage);
    font-family: "Questrial", sans-serif;
  }
  .banner {
    position: absolute;
    left: 360px;
    top: 30px;
    width: 480px;
    height: 1140px;
    background: var(--banner);
    box-shadow: 0 6px 24px rgba(0,0,0,0.12);
  }
  .brand {
    position: absolute;
    top: 42px;
    right: 32px;
    text-align: right;
    color: var(--brand-navy);
    font-weight: 400;
    line-height: 1;
  }
  .brand-name {
    display: block;
    font-size: 52px;
    letter-spacing: 1px;
  }
  .brand-tagline {
    display: block;
    font-size: 17px;
    margin-top: 4px;
  }
  .headline {
    position: absolute;
    left: 37px;
    top: 190px;
    color: var(--brand-blue);
    font-size: 38px;
    font-weight: 400;
    line-height: 1.0;
  }
  .services {
    position: absolute;
    left: 45px;
    top: 472px;
    width: 170px;
    color: var(--brand-blue);
    font-size: 26px;
    line-height: 0.95;
    list-style: none;
  }
  .services li + li {
    margin-top: 22px;
    padding-top: 18px;
    border-top: 3px solid var(--brand-blue);
  }
  .imagery {
    position: absolute;
    left: 0;
    top: 0;
    width: 480px;
    height: 1140px;
  }
  .website {
    position: absolute;
    left: 0;
    right: 0;
    top: 1036px;
    text-align: center;
    color: var(--brand-navy);
    font-size: 19px;
  }
</style>
</head>
<body>
  <main class="banner">
    <header class="brand">
      <span class="brand-name">DOLBROOK</span>
      <span class="brand-tagline">Teaching Advisory</span>
    </header>

    <h1 class="headline">Research-Based<br>Educational Products</h1>

    <svg class="imagery" viewBox="0 0 480 1140" xmlns="http://www.w3.org/2000/svg">
      <defs>
        <linearGradient id="chart-fill" x1="0" y1="0" x2="1" y2="1">
          <stop offset="0" stop-color="var(--chart-light)"/>
          <stop offset="0.55" stop-color="var(--chart-light)"/>
          <stop offset="0.56" stop-color="var(--chart-dark)"/>
          <stop offset="1" stop-color="var(--chart-dark)"/>
        </linearGradient>
        <linearGradient id="board-fill" x1="0" y1="0" x2="1" y2="1">
          <stop offset="0" stop-color="var(--chalkboard)"/>
          <stop offset="1" stop-color="var(--chalkboard-dark)"/>
        </linearGradient>
        <linearGradient id="photo-fill" x1="0" y1="0" x2="1" y2="1">
          <stop offset="0" stop-color="var(--photo-warm)"/>
          <stop offset="1" stop-color="var(--photo-cool)"/>
        </linearGradient>
      </defs>
      <polygon class="imagery-presentation" role="img"
        aria-label="Illustration of a teacher presenting research charts to an audience"
        points="139,317 385,317 267,554" fill="url(#chart-fill)"/>
      <polygon class="imagery-chalkboard" role="img"
        aria-label="Chalkboard with a drawn light bulb and a crumpled yellow paper idea"
        points="385,317 480,486 480,586 385,771 267,554" fill="url(#board-fill)"/>
      <polygon class="imagery-students" role="img"
        aria-label="Photo of students writing at their desks during an assessment"
        points="267,554 385,771 265,1008 139,787" fill="url(#photo-fill)"/>
    </svg>

    <ul class="services">
      <li>Educational Content Creation</li>
      <li>Formative Assessments</li>
    </ul>

    <p class="website">www.dolbrookteachingadvisory.com</p>
  </main>
</body>
</html>
```